BRIGHTDESK - Remote Tech Support Site

We are looking for a new very responsive and simple website for our brand Brightdesk.com - a remote technical support company.

This company supports customers Globally in different countries throughout Eur/ North America / South America / Asia etc (please keep this in mind and integrate into the idea).

Its important to us that the design is very explanatory, the customer should easily be able to figure out that we provide computer support right away ... I like one page responsive type designs as well without a bunch of menu items

Here are some similar sites we like - but still looking for a unique design that fits out brand "brightdesk" - I have upload also some layouts i like (but the designs are not important just the layouts), youll see it includes consumer business etc which is important.

VOLM.COM - I love how clean it is - nice and white easy to see everything

PLUMWIRE247.COM - also nice the layout and responsive one page design makes it easy to use

corvalfix.com - similar to plumwire design as well - you can get the idea im looking for between the two

You will notice those examples are much different then the attachments I added - again this is more of an idea for possible layouts .. attached is also the logo - could inspire color scheme / blue white black etc

Target Market(s)

Home consumers without computer knowledge , older age 45-65, small medium business ... computer repair - slow computers

Industry/Entity Type

Computer Repair

Logo Text

Brightdesk

Coding

Coded - Design and coding required

Number of Pages Required

1 page

Font styles to use
Sans Serif
Other font styles liked:
• your choice responsive

Colors

Designer to choose colors to be used in the design.

Requirements
Must have
• Clean - responsive - professional design - the name says it all - brightdesk
• CALL TO ACTIONS FOR "Get Help Now!" / "Learn More" etc
Nice to have
• We are looking for a new very responsive and simple website for our brand Brightdesk.com - a remote technical support company.
• This company supports customers Globally in different countries throughout Eur/ North America / South America / Asia etc (please keep this in mind and integrate into the idea).
• Its important to us that the design is very explanatory, the customer should easily be able to figure out that we provide computer support right away ... I like one page responsive type designs as well without a bunch of menu items
• Here are some similar sites we like - but still looking for a unique design that fits out brand "brightdesk" - I have upload also some layouts i like (but the designs are not important just the layouts), youll see it includes consumer business etc which is important.
• VOLM.COM - I love how clean it is - nice and white easy to see everything
• PLUMWIRE247.COM - also nice the layout and responsive one page design makes it easy to use
• corvalfix.com - similar to plumwire design as well - you can get the idea im looking for between the two
Should not have
• dark, packed page - bad small font -

```html
<!DOCTYPE html>
<html lang="en">
<head>
<meta charset="utf-8">
<title>Brightdesk – Remote Tech Support</title>
<link rel="stylesheet" href="https://fonts.googleapis.com/css2?family=Open+Sans:ital,wght@0,400;0,600;0,700;1,400&family=Noto+Serif:ital@1&display=swap">
<style>
:root{
  --ink:#1f1f1f;
  --text:#444;
  --muted:#666;
  --blue:#1e88e5;
  --blue-dark:#1a73d1;
  --card:#9fcdf8;
  --grey-band:#efeeee;
  --header:#2d2d2d;
  --footer:#1d2329;
  --footer-bar:#15191d;
  --white:#fff;
  --badge:#d9dde1;
}
*{box-sizing:border-box;margin:0;padding:0}
html,body{width:1200px;height:3255px;overflow:hidden}
body{font-family:"Open Sans",Arial,sans-serif;color:var(--text);background:var(--white);position:relative}
section,header,footer{position:absolute;left:0;width:1200px}
.abs{position:absolute}

/* header */
.site-header{top:0;height:94px;background:var(--header)}
.brand{left:96px;top:24px;display:flex;align-items:center;gap:10px;color:var(--white);font-weight:700;font-size:30px;letter-spacing:-.5px}
.brand-dot{width:42px;height:42px;border-radius:50%;background:var(--blue)}
.phone{right:92px;top:35px;color:var(--white);font-size:17px;display:flex;align-items:center;gap:10px}

/* hero */
.hero{top:94px;height:383px}
.hero-title{left:93px;top:38px;font-size:50px;line-height:60px;font-weight:400;color:var(--ink)}
.hero-sub{left:95px;top:162px;font-size:33px;line-height:38px;color:var(--ink)}
.hero-sub .accent{color:var(--blue)}
.btn-help{left:95px;top:275px;width:224px;height:66px;background:var(--blue);color:var(--white);font-size:30px;font-weight:600;display:flex;align-items:center;justify-content:center;border-radius:3px}
.hero-photo{left:630px;top:0;width:570px;height:383px;background:linear-gradient(120deg,#cfcac4 0%,#e9e5df 45%,#9a9ea3 100%)}

/* testimonials */
.testimonials{top:477px;height:623px}
.section-title{width:100%;text-align:center;font-size:32px;color:var(--ink);font-weight:400}
.testimonials .section-title{top:28px}
.section-lead{top:76px;width:100%;text-align:center;font-family:"Noto Serif",Georgia,serif;font-style:italic;font-size:20px;color:var(--ink)}
.review{left:178px;width:860px;height:120px}
.avatar{left:0;top:0;width:100px;height:100px;border-radius:50%;background:linear-gradient(160deg,#d9d3cc,#9b948c)}
.review-name{left:172px;top:4px;font-size:17px;font-weight:600;color:var(--blue)}
.review-name b{color:var(--ink)}
.quote-mark{left:130px;top:18px;font-family:"Noto Serif",Georgia,serif;font-size:60px;color:#aaa;line-height:1}
.review-text{left:174px;top:38px;width:650px;font-family:"Noto Serif",Georgia,serif;font-style:italic;font-size:16px;line-height:28px;color:var(--text)}
.review-text em{color:var(--blue);font-style:italic}

/* how it works */
.how{top:1100px;height:376px;background:var(--grey-band)}
.how .section-title{top:42px}
.step{width:360px;text-align:center}
.step svg{display:block;margin:0 auto}
.step h3{font-size:22px;font-weight:600;color:var(--ink);margin-top:42px}
.step p{font-size:14.5px;line-height:30px;color:var(--ink);margin:14px auto 0;width:290px}
.step.narrow p{width:265px}

/* pricing */
.pricing{top:1476px;height:557px}
.pricing .section-title{top:16px}
.accent-blue{color:var(--blue)}
.plan{top:86px;width:308px;height:398px;background:var(--card);text-align:center;color:var(--white);overflow:hidden}
.plan.featured{height:430px}
.plan-name{margin-top:40px;font-size:21px;font-weight:600;letter-spacing:.5px}
.plan-price{margin-top:28px;font-size:31px;color:var(--blue-dark);font-weight:400}
.plan-fee{font-size:14.5px;color:var(--blue-dark);margin-top:4px}
.plan-features{list-style:none;margin-top:36px;font-size:15.5px;line-height:37px}
.plan-features li:nth-child(n+2){font-weight:600}
.btn-learn{display:inline-block;margin-top:20px;width:135px;height:40px;line-height:40px;background:var(--white);color:var(--blue-dark);font-size:13px;font-weight:700;letter-spacing:.5px}
.ribbon{right:-36px;top:14px;width:130px;height:26px;background:var(--blue);color:var(--white);font-size:13px;line-height:26px;transform:rotate(45deg);text-align:center}

/* benefits */
.benefits{top:2033px;height:408px;background:var(--grey-band)}
.support-photo{left:145px;top:33px;width:508px;height:336px;background:linear-gradient(110deg,#e6ece8 0%,#f4f4f2 50%,#b9bcbf 100%)}
.benefits-title{left:712px;top:40px;font-size:35px;line-height:46px;color:var(--ink);font-weight:400}
.benefits-title strong{color:var(--blue);font-weight:600}
.benefit-list{left:712px;top:175px;list-style:none;font-size:16px;line-height:35px;color:var(--text)}
.benefit-list li::before{content:"\221A";color:var(--blue);margin-right:10px}
.btn-member{left:712px;top:317px;width:200px;height:50px;background:var(--blue);color:var(--white);font-size:14px;font-weight:700;display:flex;align-items:center;justify-content:center;letter-spacing:.5px}

/* features */
.features{top:2441px;height:473px}
.features .section-title{top:22px}
.feature{width:260px;text-align:center}
.feature .icon{height:52px;display:flex;align-items:flex-end;justify-content:center}
.feature h4{font-size:15.5px;font-weight:600;color:var(--ink);margin-top:14px}
.feature p{font-size:13.5px;line-height:26px;color:var(--text);margin:4px auto 0;width:225px}

/* footer */
.site-footer{top:2914px;height:280px;background:var(--footer);color:var(--white)}
.footer-heading{font-size:16px;font-weight:600;letter-spacing:.3px}
.footer-links{list-style:none;font-size:14.5px;line-height:29px;font-weight:600}
.seal-gold{left:98px;top:150px;width:130px;height:116px;border-radius:50%;background:radial-gradient(circle,#f1cf6d,#b88a22)}
.badge-rating{left:410px;top:76px;width:156px;height:58px;background:var(--white);border-radius:4px;border:3px solid #cfcfcf}
.badge-secure{left:414px;top:166px;width:100px;height:96px;background:var(--badge);border-radius:6px}
.newsletter-text{left:729px;top:80px;font-size:15.5px;font-weight:600}
.email-field{left:736px;top:113px;width:182px;height:30px;background:var(--white);color:var(--ink);font-size:13px;padding-left:12px;line-height:30px}
.btn-signup{left:918px;top:113px;width:82px;height:30px;background:var(--blue);color:var(--white);font-size:13px;font-weight:600;text-align:center;line-height:30px}
.follow{left:729px;top:196px;font-size:14px;font-weight:600}
.social{top:232px;width:36px;height:36px;border-radius:50%}
.footer-bar{top:3194px;height:61px;background:var(--footer-bar);color:var(--white);text-align:center;font-size:13.5px;line-height:61px;font-weight:600}
.footer-bar span{color:var(--blue)}
</style>
</head>
<body>

<header class="site-header">
  <div class="abs brand"><span class="brand-dot"></span>brightdesk</div>
  <div class="abs phone">
    <svg width="18" height="18" viewBox="0 0 24 24"><rect x="1" y="1" width="22" height="22" rx="3" fill="#fff"/><path d="M8 5c1 0 2 3 1.5 4S8 10 8.5 11.5 11 15 12.5 15.5 14 14 15 14s4 1 4 2-2 3-3 3C10 19 5 14 5 8c0-1 2-3 3-3z" fill="#2d2d2d"/></svg>
    (800) 555 - 0134
  </div>
</header>

<section class="hero">
  <h1 class="abs hero-title">It’s easy to get<br>PC &amp; Internet help...</h1>
  <p class="abs hero-sub"><span class="accent">Dedicated support</span><br>Anytime. Anywhere</p>
  <a class="abs btn-help">Get Help Now!</a>
  <div class="abs hero-photo" role="img" aria-label="Smiling older couple using a laptop together at home"></div>
</section>

<section class="testimonials">
  <h2 class="abs section-title">Testimonial</h2>
  <p class="abs section-lead">This is what customers say about us</p>

  <article class="abs review" style="top:137px">
    <div class="abs avatar" role="img" aria-label="Customer portrait"></div>
    <div class="abs quote-mark">“</div>
    <p class="abs review-name">Margot Ellery <b>- UK</b></p>
    <p class="abs review-text">I was <em>very impressed with the service provided</em> and my computer was ready to use within a few hours and so much faster.</p>
  </article>

  <article class="abs review" style="top:283px">
    <div class="abs avatar" role="img" aria-label="Customer portrait"></div>
    <div class="abs quote-mark">“</div>
    <p class="abs review-name">Daniel Whitcombe <b>- UK</b></p>
    <p class="abs review-text">I contacted them about a serious threat on my laptop, they have completely transformed the laptop, it now functions like a brand new laptop, <em>the staff were excellent, really patient and helpful, excellent service and would highly recommend</em>, thank you.</p>
  </article>

  <article class="abs review" style="top:448px">
    <div class="abs avatar" role="img" aria-label="Customer portrait"></div>
    <div class="abs quote-mark">“</div>
    <p class="abs review-name">Owen Haverly <b>- UK</b></p>
    <p class="abs review-text"><em>Offered a first class service.</em> Answered all my problems very quickly. I had been having issues with my computer for a long time and the technicians helped me with lots of patience. Their service helped me fix the issues without me having to take the computer to a shop. Thank you.</p>
  </article>
</section>

<section class="how">
  <h2 class="abs section-title">How It Works</h2>
  <div class="abs step" style="left:83px;top:103px">
    <svg width="70" height="66" viewBox="0 0 70 66" fill="none" stroke="#1e88e5" stroke-width="3"><rect x="4" y="8" width="56" height="40"/><path d="M4 40h56M26 48v8M40 48v8M18 58h30"/><path d="M54 2l10 10M64 2L54 12"/></svg>
    <h3>Free Diagnostic</h3>
    <p>Get a diagnostic, FOR FREE! Get a free consultation with our staff.</p>
  </div>
  <div class="abs step narrow" style="left:425px;top:103px">
    <svg width="70" height="66" viewBox="0 0 70 66" fill="none" stroke="#1e88e5" stroke-width="3"><rect x="4" y="8" width="56" height="40"/><path d="M4 40h56M26 48v8M40 48v8M18 58h30"/><path d="M52 8l5 5 10-11"/></svg>
    <h3>Get Fixed</h3>
    <p>Get fixed, IMMEDIATELY! Our staff will solve your computer issues right before your eyes.</p>
  </div>
  <div class="abs step narrow" style="left:740px;top:103px">
    <svg width="70" height="66" viewBox="0 0 70 66" fill="none" stroke="#1e88e5" stroke-width="3"><rect x="6" y="4" width="58" height="44"/><path d="M6 40h58M28 48v8M42 48v8M20 58h30M35 32V12M27 20l8-8 8 8"/></svg>
    <h3>Backup your information</h3>
    <p>Saving your files is now EASY! You will be able to retain your personal files without any loss of data.</p>
  </div>
</section>

<section class="pricing">
  <h2 class="abs section-title">Membership Pricing and <span class="accent-blue">Plans</span></h2>
  <div class="abs plan" style="left:117px">
    <p class="plan-name">PREMIUM</p>
    <p class="plan-price">$19.99 / Month</p>
    <p class="plan-fee">($249-$300 setup fee)</p>
    <ul class="plan-features"><li>Regular 90-Day Optimization</li><li>Unlimited 24/7 Tier 3 Technician<br>Support</li></ul>
    <a class="btn-learn">LEARN MORE</a>
  </div>
  <div class="abs plan" style="left:447px">
    <p class="plan-name">PREMIUM PLUS</p>
    <p class="plan-price">$29.99 / Month</p>
    <p class="plan-fee">($249-$300 setup fee)</p>
    <ul class="plan-features"><li>Regular 90-Day Optimization</li><li>Unlimited 24/7 Tier 3 Technician<br>Support</li></ul>
    <a class="btn-learn">LEARN MORE</a>
  </div>
  <div class="abs plan featured" style="left:777px">
    <div class="abs ribbon">Popular</div>
    <p class="plan-name">PLATINUM</p>
    <p class="plan-price">$39.99 / Month</p>
    <p class="plan-fee">($249-$300 setup fee)</p>
    <ul class="plan-features"><li>Regular 90-Day Optimization</li><li>Unlimited 24/7 Tier 3 Technician<br>Support</li><li style="font-weight:400">Online Identity Theft Protection</li></ul>
    <a class="btn-learn">LEARN MORE</a>
  </div>
</section>

<section class="benefits">
  <div class="abs support-photo" role="img" aria-label="Support technicians with headsets working at computers in a bright office"></div>
  <h2 class="abs benefits-title">Real-Time<br>Support Features and<br><strong>BENEFITS</strong></h2>
  <ul class="abs benefit-list">
    <li>24/7 Real-Time Technician Support</li>
    <li>The best Security Software in the market</li>
    <li>Regular tune-ups and optimization</li>
    <li>Setup and installation included</li>
  </ul>
  <a class="abs btn-member">BECOME A MEMBER</a>
</section>

<section class="features">
  <h2 class="abs section-title">All The Best Features, <span class="accent-blue">At The Best Price!</span></h2>

  <div class="abs feature" style="left:76px;top:94px">
    <div class="icon"><svg width="56" height="42" viewBox="0 0 56 42" fill="none" stroke="#333" stroke-width="2"><rect x="4" y="4" width="48" height="30"/><path d="M0 38h56"/><path d="M22 16h12M28 12v10" stroke="#1e88e5"/></svg></div>
    <h4>Ad Blocker</h4>
    <p>Avoid unwanted Pop-ups with the newest Ad Blocking technology.</p>
  </div>
  <div class="abs feature" style="left:339px;top:94px">
    <div class="icon"><svg width="56" height="42" viewBox="0 0 56 42" fill="none" stroke="#333" stroke-width="2"><rect x="4" y="4" width="48" height="30"/><path d="M0 38h56"/><path d="M10 28l10-10 8 6 16-14" stroke="#3a9b3a"/></svg></div>
    <h4>Regular Tune-Ups</h4>
    <p>Get a Regular Tune-Up and Optimization every 90 days.</p>
  </div>
  <div class="abs feature" style="left:601px;top:94px">
    <div class="icon"><svg width="46" height="42" viewBox="0 0 46 42" fill="none" stroke="#333" stroke-width="2"><rect x="3" y="3" width="40" height="36"/><path d="M3 11h40M9 19h28M9 25h28M9 31h18"/></svg></div>
    <h4>System Reports</h4>
    <p>Stay up to date with Real-Time System Reporting.</p>
  </div>
  <div class="abs feature" style="left:866px;top:94px">
    <div class="icon"><svg width="56" height="46" viewBox="0 0 56 46" fill="none" stroke="#333" stroke-width="2"><rect x="3" y="3" width="22" height="16" fill="#7cc47c"/><rect x="31" y="22" width="22" height="16" fill="#6aa8e8"/><path d="M14 19v10h17M42 22v-8H25"/></svg></div>
    <h4>Multiple Devices</h4>
    <p>Get support for up to 4 multiple devices. Ask about our Family</p>
  </div>

  <div class="abs feature" style="left:76px;top:282px">
    <div class="icon"><svg width="56" height="42" viewBox="0 0 56 42" fill="none" stroke="#333" stroke-width="2"><rect x="4" y="4" width="48" height="30" fill="#e6f3e6"/><path d="M0 38h56M12 14h20M12 20h28M12 26h14"/></svg></div>
    <h4>Identity Protection</h4>
    <p>Coming Soon.</p>
  </div>
  <div class="abs feature" style="left:339px;top:282px">
    <div class="icon"><svg width="30" height="50" viewBox="0 0 30 50" fill="none" stroke="#333" stroke-width="2"><rect x="3" y="2" width="24" height="46" rx="3"/><rect x="7" y="8" width="16" height="30" fill="#7cc47c"/><circle cx="15" cy="43" r="2"/></svg></div>
    <h4>Mobile Security</h4>
    <p>Coming Soon.</p>
  </div>
  <div class="abs feature" style="left:601px;top:282px">
    <div class="icon"><svg width="50" height="50" viewBox="0 0 50 50" fill="none" stroke="#333" stroke-width="2"><rect x="4" y="3" width="42" height="30"/><path d="M22 18v20l5-4 4 8 3-2-4-8h7z" fill="#7cc47c"/></svg></div>
    <h4>Cross Platform Support</h4>
    <p>One Support Plan for different types of devices.</p>
  </div>
  <div class="abs feature" style="left:866px;top:282px">
    <div class="icon"><svg width="56" height="48" viewBox="0 0 56 48" fill="none" stroke="#333" stroke-width="2"><path d="M14 34a10 10 0 0 1 0-20 14 14 0 0 1 27-2 10 10 0 0 1 3 22z"/><path d="M28 22v22M22 38l6 6 6-6"/></svg></div>
    <h4>Cloud Backup</h4>
    <p>Keep your data safe! Ask about our plans for Unlimited Cloud</p>
  </div>
</section>

<footer class="site-footer">
  <p class="abs footer-heading" style="left:93px;top:34px">PLANS</p>
  <ul class="abs footer-links" style="left:93px;top:58px"><li>Premium Plan</li><li>Premium Plus Plan</li><li>Platinum Plan</li></ul>
  <div class="abs seal-gold" role="img" aria-label="Satisfaction guarantee seal"></div>

  <p class="abs footer-heading" style="left:419px;top:34px">TRUSTED BY</p>
  <div class="abs badge-rating" role="img" aria-label="Review rating badge"></div>
  <div class="abs badge-secure" role="img" aria-label="Secure site certificate badge"></div>

  <p class="abs footer-heading" style="left:729px;top:34px">NEWSLETTER SIGNUP</p>
  <p class="abs newsletter-text">Sign up for our regular informational newsletters</p>
  <div class="abs email-field">Email</div>
  <div class="abs btn-signup">Sign Up</div>
  <p class="abs follow">Follow Us</p>
  <div class="abs social" style="left:729px;background:#3b5a9a"></div>
  <div class="abs social" style="left:777px;background:#2ba6de"></div>
</footer>

<div class="abs footer-bar" style="left:0;width:1200px">Brightdesk © 2016. All rights reserved. <span>Terms and Conditions - Refund Policy - Privacy Policy.</span></div>

</body>
</html>
```